Business Card Design for Event Planning Company

Create a business card for event planning company using our new logo. After I pick the design, I will need files made for 6 employees. Our company provides event design & logistics services as well as venue management. The font should be sans serif and complementary to the logo. I will need to know the name of the font selected for the final design. The phone numbers listed should be separated by "." not "-"

Address for the card
PO Box 318, Washington, DC 20019

Card One
Lorna Pettibone
lpettibone@galavoyant.com
202.481.7730

Card Two
Miriam Okonkwo
mokonkwo@galavoyant.com
202.556.2047

Card Three
Tessa Varnholt
tvarnholt@galavoyant.com
978.620.4471

Card Four
Robin Fess
rfess@galavoyant.com
202.718.3362

Card Five
Ada-Rose Pelletan-Uzor
adarose@galavoyant.com
202.839.1205

Card Six
Beatrix Holloway
Beatrix@galavoyant.com
202.492.6618

Target Market(s)

Corporate/Non-Profit

Industry/Entity Type

Event Planning

Contact Information for Business Card

Address for the card

Card One
Lorna Pettibone
lpettibone@galavoyant.com
202.481.7730

Card Two
Miriam Okonkwo
202.556.2047

Card Three
Tessa Varnholt
978.620.4471

Card Four
Robin Fess
rfess@galavoyant.com
202.718.3362

Card Five
Ada-Rose Pelletan-Uzor
202.839.1205

Card Six
Beatrix Holloway
202.492.6618

Font styles to use
Sans Serif

Colors

Designer to choose colors to be used in the design.

Requirements
Must have
• Two-sided with logo
Should not have
• Extra colors or be too busy

```html
<!DOCTYPE html>
<html lang="en">
<head>
<meta charset="utf-8">
<title>galavoyant business card</title>
<link rel="stylesheet" href="https://fonts.googleapis.com/css2?family=Open+Sans:wght@300;400;700&display=swap">
<style>
  :root {
    --page: #ecebe8;
    --navy-light: #0d5a7c;
    --navy-dark: #053450;
    --white: #ffffff;
    --paper-light: #ffffff;
    --paper-shade: #e4e4e4;
    --teal: #6cc0c0;
    --teal-band: #5fa9a8;
    --ink: #2b2b2b;
    --rule: rgba(255,255,255,0.55);
  }
  * { margin: 0; padding: 0; box-sizing: border-box; }
  html, body { width: 1200px; height: 1023px; overflow: hidden; }
  body {
    background: var(--page);
    font-family: "Open Sans", sans-serif;
    position: relative;
  }
  .card {
    position: absolute;
    left: 250px;
    width: 700px;
    height: 400px;
    border-radius: 22px;
    overflow: hidden;
    box-shadow: 0 10px 28px rgba(0,0,0,0.18);
  }
  /* Front */
  .card-front {
    top: 90px;
    background: radial-gradient(ellipse at 55% 35%, var(--navy-light) 0%, var(--navy-dark) 85%);
    color: var(--white);
  }
  .front-brand {
    position: absolute;
    left: 0; top: 0;
    width: 340px; height: 100%;
    display: flex;
    align-items: center;
    justify-content: center;
    gap: 14px;
  }
  .brand-dot {
    width: 30px; height: 30px;
    border-radius: 50%;
    background: var(--white);
  }
  .brand-name {
    font-weight: 300;
    font-size: 50px;
    letter-spacing: -0.5px;
    line-height: 1;
  }
  .front-divider {
    position: absolute;
    left: 352px; top: 40px;
    width: 1px; height: 320px;
    background: linear-gradient(to bottom, transparent, var(--rule) 25%, var(--rule) 75%, transparent);
  }
  .front-contact {
    position: absolute;
    left: 385px; top: 110px;
  }
  .person-name {
    font-weight: 700;
    font-size: 26px;
    margin-bottom: 18px;
  }
  .contact-list { list-style: none; }
  .contact-list li {
    display: flex;
    align-items: center;
    gap: 10px;
    font-size: 15px;
    line-height: 28px;
  }
  .contact-list svg { width: 13px; height: 13px; flex: none; }
  /* Back */
  .card-back {
    top: 533px;
    background: radial-gradient(ellipse at 40% 30%, var(--paper-light) 0%, var(--paper-shade) 100%);
  }
  .back-brand {
    position: absolute;
    left: 0; top: 0;
    width: 100%; height: 350px;
    display: flex;
    align-items: center;
    justify-content: center;
    gap: 18px;
  }
  .back-brand .brand-dot { background: var(--teal); width: 38px; height: 38px; }
  .back-brand .brand-name { color: var(--ink); font-size: 76px; }
  .tagline-band {
    position: absolute;
    left: 0; bottom: 0;
    width: 100%; height: 38px;
    background: var(--teal-band);
    color: var(--white);
    font-size: 14px;
    letter-spacing: 0.6px;
    display: flex;
    align-items: center;
    justify-content: center;
  }
</style>
</head>
<body>
  <section class="card card-front">
    <div class="front-brand">
      <span class="brand-dot"></span>
      <span class="brand-name">galavoyant</span>
    </div>
    <div class="front-divider"></div>
    <div class="front-contact">
      <h1 class="person-name">Lorna Pettibone</h1>
      <ul class="contact-list">
        <li>
          <svg viewBox="0 0 14 14"><circle cx="7" cy="7" r="6" fill="none" stroke="#fff" stroke-width="1.3"/><path d="M4.8 4.2l1.3 1.3-0.7 1 1.9 1.9 1-0.7 1.3 1.3-1 1c-2 0-4.8-2.8-4.8-4.8z" fill="#fff"/></svg>
          202.481.7730
        </li>
        <li>
          <svg viewBox="0 0 14 14"><rect x="1" y="3" width="12" height="8.5" fill="#fff"/><path d="M1 3l6 5 6-5" fill="none" stroke="#0a4a68" stroke-width="1.2"/></svg>
          lpettibone@galavoyant.com
        </li>
        <li>
          <svg viewBox="0 0 14 14"><circle cx="7" cy="7" r="6" fill="none" stroke="#fff" stroke-width="1.3"/><path d="M1 7h12M7 1c-3 3-3 9 0 12M7 1c3 3 3 9 0 12" fill="none" stroke="#fff" stroke-width="1"/></svg>
          www.galavoyant.com
        </li>
        <li>
          <svg viewBox="0 0 14 14"><path d="M7 13.5C4 9.5 2.5 7.3 2.5 5.2a4.5 4.5 0 0 1 9 0c0 2.1-1.5 4.3-4.5 8.3z" fill="#fff"/><circle cx="7" cy="5.2" r="1.6" fill="#0a4a68"/></svg>
          PO Box 318, Washington, DC 20019
        </li>
      </ul>
    </div>
  </section>

  <section class="card card-back">
    <div class="back-brand">
      <span class="brand-dot"></span>
      <span class="brand-name">galavoyant</span>
    </div>
    <p class="tagline-band">We Provides Event Design &amp; Logistics Services as well as Venue Management</p>
  </section>
</body>
</html>
```